Brightmoor Cleaning Services

need a brochure for my cleaning company. Contact info coming soon .

Target Market(s)

Cleaning Services

Industry/Entity Type

Cleaning Service

Requirements
Must have
• I attached logo for you to use.

Corporate address -
472 Kestrel Ridge W Ste 518
Larkfield, OR 97214

Phone number - 877-514-SHINE
Nice to have
• bifold brochure. I attached some samples
Should not have
• Pictures of people. Keep it clean and professional.

```html
<!DOCTYPE html>
<html lang="en">
<head>
<meta charset="utf-8">
<title>Brightmoor Cleaning Services – Bifold Brochure</title>
<link href="https://fonts.googleapis.com/css2?family=Archivo:wght@400;600;700;800&display=swap" rel="stylesheet">
<style>
  :root {
    --stage: #e6e6e9;
    --blue-deep: #0b55b0;
    --blue: #1466c4;
    --blue-mid: #1a74d2;
    --cyan: #14aee6;
    --cyan-bright: #1cb8ee;
    --ice: #c4e3f2;
    --paper: #ffffff;
    --ink: #2b2f36;
    --address: #a9d3f6;
  }
  * { box-sizing: border-box; margin: 0; padding: 0; }
  html, body { width: 1200px; height: 1200px; overflow: hidden; }
  body {
    background: var(--stage);
    font-family: "Archivo", Arial, sans-serif;
    color: var(--ink);
    position: relative;
  }
  .spread {
    position: absolute;
    left: 210px;
    width: 780px;
    height: 540px;
    display: flex;
    box-shadow: 0 10px 30px rgba(0,0,0,.12);
  }
  .spread--outside { top: 30px; }
  .spread--inside { top: 630px; }
  .page {
    position: relative;
    width: 390px;
    height: 540px;
    background: var(--paper);
    overflow: hidden;
  }
  .photo { position: absolute; }
  .block { position: absolute; }

  /* Back cover */
  .back .photo--sweeping {
    left: 0; top: 0; width: 390px; height: 330px;
    background: linear-gradient(160deg, #8a6a4d 0%, #5a3a22 45%, #3b2616 100%);
  }
  .back .band { left: 0; top: 330px; width: 390px; height: 210px; background: var(--blue-deep); }
  .back .spine-strip { left: 350px; top: 330px; width: 40px; height: 210px; background: var(--blue-mid); }
  .brand {
    position: absolute;
    display: flex; align-items: center; gap: 8px;
    font-weight: 800; color: var(--paper);
    line-height: 1.1;
  }
  .brand__dot { width: 12px; height: 12px; border-radius: 50%; background: var(--paper); flex: none; }
  .back .brand { left: 28px; top: 394px; font-size: 15px; width: 160px; }
  .address {
    position: absolute; left: 196px; top: 392px;
    font-size: 10.5px; line-height: 1.45; color: var(--address);
    font-style: normal;
  }

  /* Front cover */
  .front .photo--wiping {
    left: 0; top: 0; width: 390px; height: 370px;
    background: linear-gradient(170deg, #eef0f2 0%, #d8dadd 38%, #6b4a35 62%, #3e2a1c 100%);
  }
  .front .title-strip {
    left: 22px; top: 22px; width: 74px; height: 348px; background: var(--paper);
    display: flex; align-items: center; justify-content: center;
  }
  .title {
    writing-mode: vertical-rl; transform: rotate(180deg);
    font-weight: 700; font-size: 29px; line-height: 1.02;
    color: var(--cyan); text-transform: uppercase; letter-spacing: -0.5px;
  }
  .front .band { left: 0; top: 370px; width: 390px; height: 170px; background: var(--blue); }
  .front .accent { left: 0; top: 370px; width: 96px; height: 170px; background: var(--cyan-bright); }
  .front .square--lg { left: 332px; top: 56px; width: 30px; height: 30px; background: var(--cyan-bright); }
  .front .square--sm { left: 316px; top: 84px; width: 16px; height: 16px; background: var(--cyan-bright); }
  .front .brand { left: 150px; top: 430px; font-size: 21px; width: 220px; }

  /* Inside */
  .svc h3 {
    font-size: 11px; font-weight: 800; text-transform: uppercase;
    color: var(--cyan); margin-bottom: 5px; letter-spacing: .2px;
  }
  .svc p { font-size: 9.5px; line-height: 1.4; }
  .svc { position: absolute; padding: 16px; }
  .svc--on-color h3, .svc--on-color p { color: var(--paper); }

  .inside-left .corner { left: 0; top: 0; width: 130px; height: 140px; background: var(--cyan); }
  .inside-left .svc--one { left: 130px; top: 0; width: 260px; height: 140px; padding-top: 26px; }
  .inside-left .svc--two { left: 0; top: 140px; width: 130px; height: 240px; background: var(--ice); }
  .inside-left .photo--spray {
    left: 130px; top: 140px; width: 260px; height: 240px;
    background: linear-gradient(135deg, #e9dccb 0%, #cdb79c 50%, #c23a46 100%);
  }
  .inside-left .svc--three { left: 0; top: 380px; width: 195px; height: 160px; }
  .inside-left .svc--four { left: 195px; top: 380px; width: 195px; height: 160px; background: var(--cyan); }

  .inside-right .svc--top { left: 0; top: 0; width: 390px; height: 150px; padding: 26px 22px 0; }
  .inside-right .cols { display: flex; gap: 18px; }
  .inside-right .cols p { flex: 1; }
  .inside-right .photo--floor {
    left: 0; top: 150px; width: 360px; height: 250px;
    background: linear-gradient(180deg, #f3f4f5 0%, #dcdfe2 55%, #b9bec3 100%);
  }
  .inside-right .rule { left: 0; top: 404px; width: 360px; height: 4px; background: var(--cyan); }
  .inside-right .margin { left: 360px; top: 150px; width: 30px; height: 390px; background: #eef0f2; }
  .inside-right .svc--bottom { left: 0; top: 410px; width: 220px; height: 130px; }
  .inside-right .photo--wall {
    left: 220px; top: 418px; width: 140px; height: 110px;
    background: linear-gradient(150deg, #f0f1f2 0%, #d4d7da 70%, #e6c44a 100%);
  }
  .inside-left { border-right: 1px solid #e3e3e3; }
</style>
</head>
<body>

<section class="spread spread--outside" aria-label="Brochure outside">
  <div class="page back">
    <div class="photo photo--sweeping" role="img" aria-label="Photo of a broom and dustpan sweeping a wooden floor"></div>
    <div class="block band"></div>
    <div class="block spine-strip"></div>
    <div class="brand"><span class="brand__dot"></span><span>Brightmoor Cleaning Services</span></div>
    <address class="address">
      Corporate address:<br>
      472 Kestrel Ridge W Ste 518<br>
      Larkfield, OR 97214<br>
      Phone: 877-514-SHINE
    </address>
  </div>
  <div class="page front">
    <div class="photo photo--wiping" role="img" aria-label="Photo of a gloved hand wiping a wooden table with a cloth"></div>
    <div class="block square--lg"></div>
    <div class="block square--sm"></div>
    <div class="block title-strip"><h1 class="title">Best Cleaning<br>Service in Town</h1></div>
    <div class="block band"></div>
    <div class="block accent"></div>
    <div class="brand"><span class="brand__dot"></span><span>Brightmoor Cleaning Services</span></div>
  </div>
</section>

<section class="spread spread--inside" aria-label="Brochure inside">
  <div class="page inside-left">
    <div class="block corner"></div>
    <div class="svc svc--one">
      <h3>Service One</h3>
      <p>Routine home cleaning with dusting, vacuuming and mopping in every room, scheduled weekly or monthly to suit you.</p>
    </div>
    <div class="svc svc--two">
      <h3>Service Two</h3>
      <p>Deep kitchen and bath care that lifts grease, scale and soap film from every surface.</p>
    </div>
    <div class="photo photo--spray" role="img" aria-label="Photo of a red-gloved hand spraying cleaner in a bathroom"></div>
    <div class="svc svc--three">
      <h3>Service Three</h3>
      <p>Move-in and move-out cleans that leave each room ready for keys.</p>
    </div>
    <div class="svc svc--four svc--on-color">
      <h3>Service Four</h3>
      <p>Office cleaning after hours so your team starts fresh every morning.</p>
    </div>
  </div>
  <div class="page inside-right">
    <div class="svc svc--top">
      <h3>Service One</h3>
      <div class="cols">
        <p>Floor care for warehouses and halls, with scrubbing, sealing and polishing by trained crews.</p>
        <p>We bring our own tools and eco-safe products to every job site.</p>
      </div>
    </div>
    <div class="photo photo--floor" role="img" aria-label="Photo of a large empty warehouse floor being washed"></div>
    <div class="block rule"></div>
    <div class="block margin"></div>
    <div class="svc svc--bottom">
      <h3>Service One</h3>
      <p>Post-build cleanup that clears dust, paint spots and debris so new spaces are ready to open.</p>
    </div>
    <div class="photo photo--wall" role="img" aria-label="Photo of a white wall being wiped with a yellow glove"></div>
  </div>
</section>

</body>
</html>
```